Body therapist needs a business card

I need a card for my business which is teaching trainings in body therapy, the company is called Wellacombe Educational Group. I teach to massage therapists around Australia, South East Asia and the USA. I am attaching my logo which will guide you as to what colours I would like to have you consider. Please consult my website to find out more about what I do. www.kinetrova.com.au

My name is Gareth Wellacombe. My phone number is (03) 9157 2618 or 0412573086. email is info@kinetrova.com.au

```html
<!DOCTYPE html>
<html lang="en">
<head>
<meta charset="utf-8">
<title>Wellacombe Educational Group – Business Card</title>
<link rel="stylesheet" href="https://fonts.googleapis.com/css2?family=Montserrat:wght@300;400&family=Open+Sans:wght@400&display=swap">
<style>
  :root {
    --stage: #e6e7e9;
    --card-white: #ffffff;
    --card-dark: #2b3236;
    --brown: #8b4d22;
    --brown-text: #a9643a;
    --lime: #c8d92c;
    --red: #a61c24;
    --ink: #4b4f54;
    --white: #ffffff;
  }
  * { box-sizing: border-box; margin: 0; padding: 0; }
  html, body { width: 1200px; height: 900px; overflow: hidden; }
  body {
    background: var(--stage);
    position: relative;
    font-family: "Open Sans", Arial, sans-serif;
  }
  .card {
    position: absolute;
    left: 320px;
    width: 560px;
    height: 320px;
    box-shadow: 0 6px 18px rgba(0,0,0,0.18);
    overflow: hidden;
  }
  /* Front */
  .card--front { top: 100px; background: var(--card-white); }
  .front__brand {
    position: absolute;
    left: 70px; top: 118px;
    display: flex; align-items: center; gap: 10px;
  }
  .brand-dot {
    width: 22px; height: 22px; border-radius: 50%;
    background: var(--brown);
  }
  .brand-name {
    font-family: "Montserrat", Arial, sans-serif;
    font-weight: 400;
    font-size: 22px;
    color: var(--brown);
    letter-spacing: 0.5px;
  }
  .front__divider {
    position: absolute;
    left: 262px; top: 96px;
    width: 2px; height: 96px;
    background: var(--lime);
  }
  .front__details {
    position: absolute;
    left: 282px; top: 94px;
  }
  .person-name {
    font-family: "Montserrat", Arial, sans-serif;
    font-weight: 400;
    font-size: 20px;
    color: var(--brown-text);
    line-height: 1.15;
  }
  .person-role {
    font-size: 15px; color: var(--ink); margin-bottom: 4px;
  }
  .contact {
    list-style: none;
    font-size: 15px; color: var(--ink);
  }
  .contact li { display: flex; align-items: center; gap: 7px; line-height: 1.45; }
  .contact svg { width: 13px; height: 13px; flex: none; }

  /* Back */
  .card--back { top: 480px; background: var(--card-dark); }
  .back__pattern {
    position: absolute; inset: 0;
    background: radial-gradient(ellipse at 50% 45%, #343d36 0%, var(--card-dark) 75%);
  }
  .back__brand {
    position: absolute;
    left: 0; right: 0; top: 112px;
    display: flex; flex-direction: column; align-items: center; gap: 6px;
  }
  .back__row { display: flex; align-items: center; gap: 12px; }
  .back__dot {
    width: 26px; height: 26px; border-radius: 50%;
    background: var(--lime);
  }
  .back__name {
    font-family: "Montserrat", Arial, sans-serif;
    font-weight: 300;
    font-size: 36px;
    color: var(--white);
    letter-spacing: 2px;
  }
  .back__tagline {
    font-family: "Montserrat", Arial, sans-serif;
    font-weight: 300;
    font-size: 13px;
    color: var(--white);
    letter-spacing: 0.5px;
    padding-left: 38px;
  }
</style>
</head>
<body>
  <section class="card card--front" aria-label="Business card front">
    <div class="front__brand">
      <span class="brand-dot"></span>
      <span class="brand-name">Wellacombe</span>
    </div>
    <div class="front__divider"></div>
    <div class="front__details">
      <p class="person-name">Gareth Wellacombe</p>
      <p class="person-role">Teacher</p>
      <ul class="contact">
        <li>
          <svg viewBox="0 0 16 16" aria-hidden="true"><circle cx="8" cy="8" r="7" fill="none" stroke="var(--red)" stroke-width="1.5"/><path d="M5 4.5l1.5 0 .8 2-1 .8a5 5 0 0 0 2.4 2.4l.8-1 2 .8v1.5a1 1 0 0 1-1 1A6 6 0 0 1 4 5.5a1 1 0 0 1 1-1z" fill="var(--red)"/></svg>
          (03) 9157 2618
        </li>
        <li>
          <svg viewBox="0 0 16 16" aria-hidden="true"><rect x="1" y="3" width="14" height="10" fill="none" stroke="var(--red)" stroke-width="1.5"/><path d="M1 3l7 6 7-6" fill="none" stroke="var(--red)" stroke-width="1.5"/></svg>
          info@kinetrova.com.au
        </li>
        <li>
          <svg viewBox="0 0 16 16" aria-hidden="true"><circle cx="8" cy="8" r="7" fill="var(--red)"/><path d="M1 8h14M8 1v14M3 4.5h10M3 11.5h10" stroke="#fff" stroke-width="1"/><ellipse cx="8" cy="8" rx="3" ry="7" fill="none" stroke="#fff" stroke-width="1"/></svg>
          www.kinetrova.com.au
        </li>
      </ul>
    </div>
  </section>

  <section class="card card--back" aria-label="Business card back">
    <div class="back__pattern" role="img" aria-label="Repeating pattern of soft olive and deep red circles over dark slate"></div>
    <div class="back__brand">
      <div class="back__row">
        <span class="back__dot"></span>
        <span class="back__name">Wellacombe</span>
      </div>
      <span class="back__tagline">Educational Group</span>
    </div>
  </section>
</body>
</html>
```